Photography Prints Business Card Design

Background info: Nature, flower, landscape,  macro, wildlife photographer. Shoot color and B&W images. Sell prints at juried fine art shows.
Looking for two-sided, clean, memorable design with creative use of my initials, DK.   I like the DK symbol in the my logo. Just use the DK symbol. Do not leave the underlying text as uploaded by me. I do not like the serif font and positioning of the words!  Either  remove the small print "Dorian Kessler Photography" under the logo,  or change to a sans serif font, or reposition with "Dorian Kessler" above "Photography" which seems to work with serif fonts.
Target Market(s)
Sophisticated art buyers, post-college to middle age
Industry/Entity Type
Business
Contact Information for Business Card
Dorian Kessler Photography
842 Harrow Bend CT
Larkfield, NC 27127
(336) 555-0148
www.doriankessler.com
PW:kesslerphoto
dorian@doriankessler.com
If using just one line address, make sure there is a comma after  "CT" in street address. For example:
842 Harrow Bend CT, Larkfield, NC 27127
Requirements
Must have
- 1.Two-sided card submitted as one design.
2. Must use the DK symbol in my logo.
3. Do not leave the text "Dorian Kessler Photography" under the DK symbol in the logo uploaded by me. I do not like that serif font or the positioning of the words! Either remove the small print "Dorian Kessler Photography" under the logo entirely, or change text to a sans serif font, or reposition text with "Dorian Kessler" above "Photography" which seems to work with serif fonts.
Nice to have
- Can use my DK logo (three file types uploaded: AI, PSD, TIF)  I  like the attached B&W water droplet photo.  My pictures on my website, www.doriankkessler.com  can also be used.  Possible use of Pinwave logo with (either the "f" alone or the square blue icon with white "f") my PW page short url name: kesslerphoto.
Should not have
- 1.No icons or pictures  of camera or lenses or other photographic gear or film strips.
2. No QR or other "barcode" type symbols.
3. No outlining of my logo symbol (drop shadow possibly).
4. No decorative or outlined fonts.
5. I am not a fan of most script fonts.
6. No play on "Kessler" such as snow or other winter season symbols.
7. Do not keep the original text, "Dorian Kessler Photography" under DK logo. Change it or remove it entirely.

```html
<!DOCTYPE html>
<html lang="en">
<head>
<meta charset="utf-8">
<title>Dorian Kessler Photography – Business Card</title>
<link rel="stylesheet" href="https://fonts.googleapis.com/css2?family=Open+Sans:wght@400;600&display=swap">
<style>
  :root {
    --stage: #e9e6e2;
    --card-dark: #3b3636;
    --ink-soft: #a19b9a;
    --ink-mark: #8f8989;
    --photo-deep: #2c2929;
    --photo-mid: #6e6b6b;
    --photo-light: #c9c7c7;
    --mark-dark: #2a2626;
  }
  * { box-sizing: border-box; margin: 0; padding: 0; }
  html, body {
    width: 1200px; height: 1000px; overflow: hidden;
    background: var(--stage);
    font-family: "Open Sans", sans-serif;
  }
  .stage {
    width: 1200px; height: 1000px;
    display: flex; flex-direction: column;
    align-items: center; justify-content: center; gap: 22px;
  }
  .card {
    position: relative;
    width: 820px; height: 469px;
    overflow: hidden;
    box-shadow: 0 6px 18px rgba(0,0,0,.18);
  }
  /* Back: contact side */
  .card-back { background: var(--card-dark); }
  .contact {
    position: absolute; left: 110px; top: 80px; width: 480px;
    text-align: center; color: var(--ink-soft);
    font-size: 24px; line-height: 1.45;
  }
  .contact .studio-name {
    font-weight: 600; font-size: 31px; letter-spacing: .5px;
    margin-bottom: 6px; white-space: nowrap;
  }
  .monogram {
    position: absolute;
    font-family: "Open Sans", sans-serif; font-weight: 600;
    letter-spacing: -2px; line-height: 1;
  }
  .card-back .monogram {
    right: 70px; top: 60px; font-size: 92px; color: var(--ink-mark);
  }
  /* Front: photo side */
  .card-front .photo {
    position: absolute; inset: 0;
    background:
      radial-gradient(ellipse 60% 25% at 55% 30%, rgba(220,220,220,.35), transparent 70%),
      linear-gradient(168deg, var(--photo-deep) 0%, var(--photo-deep) 28%, var(--photo-mid) 45%, var(--photo-light) 78%, #b4b2b2 100%);
  }
  .card-front .monogram {
    right: 70px; top: 150px; font-size: 120px; color: var(--mark-dark);
  }
</style>
</head>
<body>
  <main class="stage">
    <section class="card card-back" aria-label="Card back with contact details">
      <div class="contact">
        <p class="studio-name">Dorian Kessler Photography</p>
        <p>842 Harrow Bend CT, Larkfield</p>
        <p>NC 27190</p>
        <p>(336) 555-0148</p>
        <p>dorian@doriankessler.com</p>
        <p>PW:kesslerphoto</p>
        <p>www.doriankessler.com</p>
      </div>
      <span class="monogram">DK</span>
    </section>

    <section class="card card-front" aria-label="Card front">
      <div class="photo" role="img" aria-label="Black and white macro photograph of water droplets beading on a leaf surface"></div>
      <span class="monogram">DK</span>
    </section>
  </main>
</body>
</html>
```